R J Penn Accounting & SMSF Auditing needs a Web Site Design

I need some examples of what a web design can look like for my business.
The business name is above and I have already registered a domain name of www.penn-smsf.com.au
I have attached my current letterhead and business cards and would like to maintain these colours basically Red on White with some black

```html
<!DOCTYPE html>
<html lang="en">
<head>
<meta charset="utf-8">
<title>R J Penn Accounting &amp; SMSF Auditing</title>
<link href="https://fonts.googleapis.com/css2?family=Open+Sans:wght@400;600&family=Roboto+Slab:wght@400;700&family=Roboto+Condensed:wght@400;700&display=swap" rel="stylesheet">
<style>
:root{
  --red:#c5122f;
  --dark:#4a4944;
  --ink:#222;
  --text:#555;
  --hero:#ebebeb;
  --white:#fff;
  --rule:#ddd;
}
*{box-sizing:border-box;margin:0;padding:0}
html,body{width:911px;height:1200px;overflow:hidden;background:var(--white)}
body{font-family:"Open Sans",Arial,sans-serif;color:var(--text);position:relative}
.abs{position:absolute}

/* header */
.brand-name{left:61px;top:16px;font:700 27px/1 "Roboto Slab",Georgia,serif;color:var(--red);letter-spacing:.5px}
.brand-role{left:61px;top:52px;width:214px;text-align:center;font-size:12.5px;color:#333}
.brand-cert{left:61px;top:69px;width:214px;text-align:center;font-size:12.5px;color:var(--red)}
.phone{left:694px;top:25px;display:flex;align-items:center;gap:8px}
.phone-num{font:600 22px/1 "Open Sans",Arial,sans-serif;color:#444;letter-spacing:.5px}
.phone-note{left:660px;top:61px;width:191px;text-align:right;font:600 10.5px/1 "Open Sans",Arial,sans-serif;color:#444}

/* nav */
.nav{left:0;top:105px;width:911px;height:35px;background:var(--dark)}
.nav a{position:absolute;top:0;height:35px;font:700 13.5px/35px "Roboto Slab",Georgia,serif;color:var(--white);text-decoration:none;text-transform:uppercase;white-space:nowrap}
.nav a.active{background:var(--red);width:80px;text-align:center}
.nav .search{position:absolute;left:816px;top:0;width:35px;height:35px;background:var(--red);display:flex;align-items:center;justify-content:center}

/* hero */
.hero{left:0;top:140px;width:911px;height:357px;background:var(--hero)}
.hero-title{left:100px;top:92px;width:264px;text-align:center;font:700 26px/32px "Roboto Slab",Georgia,serif;color:var(--red)}
.hero-sub{left:80px;top:194px;width:304px;text-align:center;font:600 14px/20px "Open Sans",Arial,sans-serif;color:#444}
.frame{background:var(--white);box-shadow:0 2px 6px rgba(0,0,0,.18)}
.dots{left:577px;top:318px;display:flex;gap:8px}
.dots span{width:12px;height:12px;border-radius:50%;display:flex;align-items:center;justify-content:center}
.dots span::after{content:"";width:8px;height:8px;border-radius:50%;background:#3c3c3a}
.dots span.on{border:2px solid var(--red)}
.dots span.on::after{background:transparent}

/* features */
.features{left:0;top:497px;width:911px;height:124px;background:var(--red)}
.feature{position:absolute;top:20px;width:240px;color:var(--white)}
.feature h3{display:flex;align-items:center;gap:7px;font:700 19px/1 "Roboto Slab",Georgia,serif;margin-bottom:10px;white-space:nowrap}
.feature p{font-size:11.5px;line-height:16px;text-align:center;width:220px}

/* welcome */
.welcome-img{left:62px;top:654px;width:156px;height:121px;background:linear-gradient(135deg,#3a1e10,#8a4a22 55%,#4a2612);border:1px solid #333}
.welcome{left:234px;top:652px;width:620px}
.welcome h2,.col h2{font:700 15px/1 "Roboto Slab",Georgia,serif;color:var(--ink);text-transform:uppercase;margin-bottom:7px}
.welcome p{font-size:10px;line-height:16px}
.read-more{display:inline-block;margin-top:8px;font-size:10px;color:#222;text-decoration:underline}
.divider{left:62px;top:799px;width:790px;border-top:1px dotted #ccc}

/* columns */
.col{position:absolute;top:822px;width:254px}
.col p{font-size:10.2px;line-height:16px;text-align:justify}
.post{position:absolute;left:0;width:254px}
.post-img{position:absolute;left:1px;top:0;width:76px;height:66px;border:1px solid #ccc}
.post-body{position:absolute;left:85px;top:0;width:170px}
.post-body h4{font:700 11px/1 "Roboto Slab",Georgia,serif;color:var(--ink);margin-bottom:6px}
.post-body p{font-size:10.4px;line-height:14px;text-align:left}
.post-meta{font-size:11px;color:#666;margin-top:4px}
.areas{list-style:none}
.areas li{position:relative;height:26px;line-height:26px;font-size:10.5px;color:#444;padding-left:9px;border-bottom:1px solid #e6e6e6;white-space:nowrap}
.areas li::before{content:"";position:absolute;left:0;top:10px;border-left:4px solid #888;border-top:3px solid transparent;border-bottom:3px solid transparent}
.areas li.first{color:#222}
.areas li.first::before{border-left-color:#222}
.btn{position:absolute;top:1014px;width:68px;height:23px;text-align:center;font:600 10px/23px "Open Sans",Arial,sans-serif;color:var(--white);text-decoration:none}
.btn.red{background:var(--red)}
.btn.dark{background:var(--dark)}

/* newsletter */
.newsletter{left:0;top:1069px;width:911px;height:63px;background:var(--red)}
.news-title{position:absolute;left:232px;top:21px;font:400 17px/1 "Roboto Condensed",Arial Narrow,sans-serif;color:var(--white);white-space:nowrap}
.news-input{position:absolute;left:422px;top:17px;width:187px;height:30px;background:var(--white);font-size:10.5px;color:#777;line-height:30px;padding-left:15px}
.news-btn{position:absolute;left:625px;top:17px;width:57px;height:30px;background:#000;color:var(--white);font:600 10.5px/30px "Open Sans",Arial,sans-serif;text-align:center}

/* footer */
.footer{left:0;top:1132px;width:911px;height:68px;background:var(--dark)}
.foot-links{position:absolute;left:60px;top:14px;font-size:10.5px;color:#ddd}
.foot-links a{color:#ddd;text-decoration:none}
.foot-links a.current{color:var(--white)}
.foot-links .sep{margin:0 7px}
.copyright{position:absolute;left:60px;top:36px;font-size:10.5px;color:#ccc}
.social{position:absolute;left:714px;top:25px;display:flex;gap:5px}
.social span{width:19px;height:19px}
</style>
</head>
<body>

<header>
  <div class="abs brand-name">R J Penn</div>
  <div class="abs brand-role">Director – Principal Adviser</div>
  <div class="abs brand-cert">Registered SMSF Auditor</div>
  <div class="abs phone">
    <svg width="26" height="30" viewBox="0 0 26 30" aria-hidden="true">
      <path d="M6 2c2 0 4 5 4 7s-3 2-3 4 3 7 5 8 2-2 4-2 6 3 6 5-3 4-5 4C10 28 1 16 2 7 2 4 4 2 6 2z" fill="var(--red)"/>
      <path d="M15 5a8 8 0 0 1 7 7M15 1a12 12 0 0 1 10 10" stroke="var(--red)" stroke-width="2" fill="none"/>
    </svg>
    <span class="phone-num">0491570156</span>
  </div>
  <div class="abs phone-note">CALL FOR FREE CONSULTATION</div>
</header>

<nav class="abs nav">
  <a class="active" href="#" style="left:62px">Home</a>
  <a href="#" style="left:163px">About Us</a>
  <a href="#" style="left:269px">Services</a>
  <a href="#" style="left:372px">Tax Planning</a>
  <a href="#" style="left:510px">Corporate</a>
  <a href="#" style="left:630px">Finance</a>
  <a href="#" style="left:727px">Contact Us</a>
  <span class="search">
    <svg width="18" height="18" viewBox="0 0 18 18" aria-hidden="true"><circle cx="7.5" cy="7.5" r="5.5" stroke="#fff" stroke-width="2.6" fill="none"/><path d="M11.5 11.5l5 5" stroke="#fff" stroke-width="3" stroke-linecap="round"/></svg>
  </span>
</nav>

<section class="abs hero">
  <h1 class="abs hero-title">ACCOUNTANTS<br>AND<br>AUDITORS</h1>
  <p class="abs hero-sub">Lorem ipsum dolor sit amet consecte uradipiscingelitivamus tincidunt</p>

  <div class="abs frame" style="left:420px;top:68px;width:300px;height:222px;transform:rotate(-16deg)">
    <div style="position:absolute;left:12px;top:12px;right:12px;bottom:12px;background:linear-gradient(135deg,#b6c6d2,#8aa0b0)"></div>
  </div>
  <div class="abs frame" style="left:448px;top:56px;width:320px;height:230px;transform:rotate(-8deg)">
    <div style="position:absolute;left:12px;top:12px;right:12px;bottom:12px;background:linear-gradient(135deg,#e0a020,#5a6b3a)"></div>
  </div>
  <div class="abs frame" style="left:486px;top:64px;width:335px;height:224px">
    <div role="img" aria-label="Accountant working at a desk with a calculator and files" style="position:absolute;left:12px;top:11px;width:312px;height:201px;background:linear-gradient(120deg,#d8dadc,#f2f2f2 55%,#8e9aa6)"></div>
  </div>

  <div class="abs dots"><span class="on"></span><span></span><span></span><span></span></div>
</section>

<section class="abs features">
  <div class="feature" style="left:61px">
    <h3><svg width="26" height="22" viewBox="0 0 26 22" aria-hidden="true"><rect x="1" y="5" width="24" height="16" rx="2" fill="#fff"/><rect x="9" y="1" width="8" height="5" rx="1" stroke="#fff" stroke-width="2" fill="none"/><rect x="1" y="11" width="24" height="2" fill="var(--red)"/><rect x="11" y="10" width="4" height="4" fill="#fff"/></svg>Save Money!</h3>
    <p>Lorem ipsum dolor sit amet, consectetur adipisicing elit, sed do eiusmod tempor incididunt ut labore et dolore magna..</p>
  </div>
  <div class="feature" style="left:345px">
    <h3><svg width="26" height="26" viewBox="0 0 26 26" aria-hidden="true"><circle cx="13" cy="14" r="10.5" stroke="#fff" stroke-width="2.2" fill="none"/><rect x="11" y="1" width="4" height="3" fill="#fff"/><path d="M13 14V8" stroke="#fff" stroke-width="2.4"/><circle cx="13" cy="14" r="2" fill="#fff"/></svg>Collaborate!</h3>
    <p>Lorem ipsum dolor sit amet, consectetur adipisicing elit, sed do eiusmod tempor incididunt ut labore et dolore magna..</p>
  </div>
  <div class="feature" style="left:632px">
    <h3><svg width="30" height="28" viewBox="0 0 30 28" aria-hidden="true"><path d="M6 24C4 12 14 3 28 2c0 14-8 22-20 21" stroke="#fff" stroke-width="2" fill="none"/><path d="M2 27L22 8M10 17h7M14 13h6M12 15V9M17 10V5" stroke="#fff" stroke-width="1.6" fill="none"/></svg>Grow your Businesss</h3>
    <p>Lorem ipsum dolor sit amet, consectetur adipisicing elit, sed do eiusmod tempor incididunt ut labore et dolore magna..</p>
  </div>
</section>

<div class="abs welcome-img" role="img" aria-label="Wooden judge's gavel in front of law books"></div>
<section class="abs welcome">
  <h2>Welcome to our website</h2>
  <p>Lorem ipsum dolor sit amet, consectetur adipiscing elit. Ut gravida sod ales lacus at pretium. Nunc mollis odio ac turpis adipiscing euismod. Cras vitaes ollicitudin sem.Vestibulum ante ipsum primis in faucibus orci luctus et ultri ces posuere cubilia Curae; Aenean id ligula porttitor, ornare ligula ele men tum, luctus metus.</p>
  <p>Lorem ipsum dolor sit amet, consectetur adipiscing elit. Ut gravida sod ales lacus at pretium. Nunc mollis odio ac turpis adipiscing euismod. Cras vitaes ollicitudin sem.Vestibulum ante ipsum primis in faucibus orci luctus et ultri ces posuere cubilia Curae; Aenean</p>
  <a class="read-more" href="#">Read More ›</a>
</section>
<div class="abs divider"></div>

<section class="col" style="left:62px">
  <h2>Who we are</h2>
  <p>Lorem ipsum dolor sit amet consectetur adipiscing elit. Ut gravida sod ales lacus at pretium. Nunc mollis odio ac turpis adipiscing euismod. Cras vitaes ollicitudin sem.Vestibulum ante ipsum primis in faucibus orci luctus porttitor,</p>
  <p>Lorem ipsum dolor sit amet consectetur adipiscing elit. Ut gravida sod ales lacus at pretium. Nunc mollis odio ac turpis adipiscing euismod. Cras vitaes ollicitudin sem.Vestibulum ante ipsum primis in faucibus orci luctus et ultri ces posuere.</p>
</section>

<section class="col" style="left:330px">
  <h2>Latest blog</h2>
  <article class="post" style="top:24px">
    <div class="post-img" role="img" aria-label="Colleagues in a business seminar" style="background:linear-gradient(135deg,#e9ecef,#9aa3ad)"></div>
    <div class="post-body">
      <h4>Law Coahcing Seminar</h4>
      <p>Lorem ipsum dolor sit amet, conse tetur adipiscing elit....</p>
      <div class="post-meta">Aug 10rd, 2014 | 1 Comment</div>
    </div>
  </article>
  <article class="post" style="top:106px">
    <div class="post-img" role="img" aria-label="Businesswoman at her desk" style="background:linear-gradient(135deg,#d9dcdf,#6f6c6a)"></div>
    <div class="post-body">
      <h4>Laywar Sechdule</h4>
      <p>Lorem ipsum dolor sit amet, conse ctetur adipiscing elit....</p>
      <div class="post-meta">Aug 12rd, 2014 | 1 Comment</div>
    </div>
  </article>
</section>

<section class="col" style="left:599px;width:253px">
  <h2 style="margin-bottom:2px">Practice areas</h2>
  <ul class="areas">
    <li class="first">Assistance provided to our customers payment</li>
    <li>Financial and Management Accounting</li>
    <li>Salaries and Human Resource</li>
    <li>Real estate and landlord tenant law</li>
    <li>Accounting Know-how</li>
    <li>Asset Protection</li>
  </ul>
</section>

<a class="btn red" href="#" style="left:247px">View All</a>
<a class="btn dark" href="#" style="left:516px">View All</a>
<a class="btn dark" href="#" style="left:784px">View All</a>

<section class="abs newsletter">
  <svg class="abs" style="left:192px;top:24px" width="23" height="17" viewBox="0 0 23 17" aria-hidden="true"><rect x="1" y="1" width="21" height="15" stroke="#fff" stroke-width="1.5" fill="none"/><path d="M1 1l10.5 9L22 1M1 16l8-7M22 16l-8-7" stroke="#fff" stroke-width="1.5" fill="none"/></svg>
  <div class="news-title">Subscrie For Our Newsletter</div>
  <div class="news-input">Email Address</div>
  <div class="news-btn">SIGN UP</div>
</section>

<footer class="abs footer">
  <div class="foot-links">
    <a class="current" href="#">Home</a><span class="sep">/</span><a href="#">About</a><span class="sep">/</span><a href="#">Services</a><span class="sep">/</span><a href="#">Tax Planning</a><span class="sep">/</span><a href="#">Corporate</a><span class="sep">/</span><a href="#">Finance</a><span class="sep">/</span><a href="#">Contact</a>
  </div>
  <div class="copyright">Copyright © 2014 rjpenn.All Rights Reserved</div>
  <div class="social">
    <span style="background:#3b5a98"></span>
    <span style="background:#2a9fe0"></span>
    <span style="background:#1a6fa8"></span>
    <span style="background:#d9442e"></span>
    <span style="background:#c8202a"></span>
    <span style="background:#d43a2a"></span>
  </div>
</footer>

</body>
</html>
```